Brasko Construction Business Card

I need a business card design for my company.
We are a construction/machinery company.
I would like to see my logo on the front of the card and my details on the other side
I would like the card to be black or dark grey in colour,with my logo as i send it or modified with a lighter blue colour
I would like to see the design kept fairly simple,but eye catching at the same time
Industry/Entity Type
Business
Contact Information for Business Card
Name
Phone Number
Address
Email
Colors
00a990
1b1b1b
000000
474747
ececec

```html
<!DOCTYPE html>
<html lang="en">
<head>
<meta charset="UTF-8">
<title>Brasko Construction Business Card</title>
<link href="https://fonts.googleapis.com/css2?family=Open+Sans:wght@400;600;700&display=swap" rel="stylesheet">
<style>
  :root {
    --teal: #00a990;
    --charcoal: #1b1b1b;
    --black: #000000;
    --graphite: #474747;
    --white: #ffffff;
    --backdrop: #ececec;
  }
  * { box-sizing: border-box; margin: 0; padding: 0; }
  html, body {
    width: 1200px; height: 900px; overflow: hidden;
    background: var(--backdrop);
    font-family: "Open Sans", Arial, sans-serif;
  }
  .canvas { position: relative; width: 1200px; height: 900px; }
  .card {
    position: absolute; left: 290px;
    width: 620px; height: 354px;
    overflow: hidden;
    box-shadow: 0 10px 28px rgba(0,0,0,0.22);
  }

  /* Logo side */
  .card--logo { top: 72px; background: var(--charcoal); }
  .machine-art {
    position: absolute; inset: 0;
    background: radial-gradient(ellipse at 64% 32%, var(--graphite) 0%, #333333 34%, rgba(27,27,27,0) 70%);
  }
  .card--logo .wordmark {
    position: absolute; left: 44px; bottom: 62px;
    color: var(--teal);
  }

  /* Details side */
  .card--details { top: 474px; background: var(--black); }
  .card--details .top {
    position: absolute; left: 0; top: 0; width: 100%; height: 190px;
    background: linear-gradient(180deg, var(--charcoal), var(--black));
    display: flex; align-items: center; justify-content: center;
    padding-left: 70px;
  }
  .card--details .wordmark { color: var(--teal); }

  .wordmark {
    display: flex; align-items: center; gap: 14px;
    font-weight: 700; font-size: 34px; line-height: 1.05;
    text-transform: uppercase; letter-spacing: 1px;
  }
  .wordmark .mark-square { width: 40px; height: 40px; background: currentColor; flex: none; }
  .wordmark .name-stack { display: flex; flex-direction: column; }
  .wordmark .name-stack span:last-child { font-size: 17px; letter-spacing: 4.6px; }

  .band {
    position: absolute; left: 0; bottom: 0; width: 100%; height: 164px;
    background: var(--teal); color: var(--white);
    padding: 26px 40px 0 142px;
  }
  .band .row { display: flex; justify-content: space-between; }
  .person-name { font-weight: 700; font-size: 21px; line-height: 1.2; }
  .person-role { font-size: 15px; padding-left: 36px; }
  .contacts { list-style: none; font-size: 14px; line-height: 1.7; }
  .contacts li { display: flex; align-items: center; gap: 9px; }
  .contacts svg { width: 13px; height: 13px; fill: var(--white); }
  .address { margin-top: 22px; font-size: 16px; }
</style>
</head>
<body>
<main class="canvas">
  <section class="card card--logo">
    <div class="machine-art" role="img" aria-label="Faint large excavator arm illustration in dark grey tones"></div>
    <div class="wordmark">
      <span class="mark-square"></span>
      <div class="name-stack"><span>Brasko</span><span>Construction</span></div>
    </div>
  </section>

  <section class="card card--details">
    <div class="top">
      <div class="wordmark">
        <span class="mark-square"></span>
        <div class="name-stack"><span>Brasko</span><span>Construction</span></div>
      </div>
    </div>
    <div class="band">
      <div class="row">
        <div>
          <p class="person-name">Daniel Marsh</p>
          <p class="person-role">Managing Director</p>
        </div>
        <ul class="contacts">
          <li><svg viewBox="0 0 24 24"><path d="M6.6 10.8a15.1 15.1 0 0 0 6.6 6.6l2.2-2.2c.3-.3.7-.4 1-.2 1.1.4 2.3.6 3.6.6.6 0 1 .4 1 1V20c0 .6-.4 1-1 1A17 17 0 0 1 3 4c0-.6.4-1 1-1h3.5c.6 0 1 .4 1 1 0 1.3.2 2.5.6 3.6.1.3 0 .7-.2 1z"/></svg>(044)-555-0182</li>
          <li><svg viewBox="0 0 24 24"><path d="M2 5h20v14H2z M2 5l10 8 10-8" fill="none" stroke="#fff" stroke-width="2"/><path d="M2 5h20l-10 8z"/></svg>info@braskobuild.com</li>
        </ul>
      </div>
      <p class="address">48 Quarry Lane, Millbrook, Eastland 204816</p>
    </div>
  </section>
</main>
</body>
</html>
```